Business Cards that are elegant and wow

I want to create and print business cards that represent my brand and stand out from the rest. We want to ensure they stay in our branding and the integrity is not lost. I am happy to look at different shapes like square etc.

It will be printed on very thick cards and will be stylish .

I want to create and print business cards that represent my brand and stand out from the rest. We want to ensure they stay in ur branding and the integrity is not lost. I am happy to look at different shapes like square etc.

Target Market(s)

real estate professionals

Industry/Entity Type

Real Estate

Contact Information for Business Card

Maren Holt
hello@brightfernrealty.com.au
brightfernrealty.com.au
0487 316 252 (SMS)

Colors

Designer to choose colors to be used in the design.

Requirements
Must have
• My logo
• email
• website
• Name
Nice to have
• I like the idea of printing with foil or spot gloss. You want it to stand out in a sea.
Should not have
• I would like you to stay in my colour themes. Don't change the colour of my logo

```html
<!DOCTYPE html>
<html lang="en">
<head>
<meta charset="utf-8">
<title>Bright Fern Realty – Business Card</title>
<link rel="stylesheet" href="https://fonts.googleapis.com/css2?family=Lato:wght@400;700&family=Roboto:wght@400&display=swap">
<style>
  :root {
    --backdrop: #e6e6e6;
    --card-white: #f4f4f4;
    --brand-pink: #e0305f;
    --brand-blue: #1a9ad6;
    --accent-green: #97ad4c;
    --accent-blue: #0b8ac1;
    --text-white: #ffffff;
  }
  * { margin: 0; padding: 0; box-sizing: border-box; }
  html, body {
    width: 1200px;
    height: 900px;
    overflow: hidden;
    background: var(--backdrop);
  }
  .business-card {
    position: absolute;
    left: 75px;
    top: 150px;
    width: 1050px;
    height: 600px;
    background: var(--card-white);
    box-shadow: 0 6px 18px rgba(0,0,0,0.18);
    overflow: hidden;
  }
  .card-art { display: block; width: 1050px; height: 600px; }
  .brand-name {
    font-family: "Lato", sans-serif;
    font-weight: 700;
    fill: var(--brand-blue);
  }
  .agent-name {
    font-family: "Lato", sans-serif;
    font-weight: 700;
    font-size: 70px;
    fill: var(--text-white);
  }
  .contact-line {
    font-family: "Roboto", sans-serif;
    font-size: 24px;
    letter-spacing: 1.2px;
    fill: var(--text-white);
  }
  .contact-icon {
    fill: none;
    stroke: var(--brand-blue);
    stroke-width: 2;
  }
</style>
</head>
<body>
  <div class="business-card">
    <svg class="card-art" viewBox="0 0 1050 600" xmlns="http://www.w3.org/2000/svg">
      <defs>
        <filter id="block-shadow" x="-10%" y="-10%" width="130%" height="130%">
          <feDropShadow dx="5" dy="0" stdDeviation="3" flood-color="#000" flood-opacity="0.35"/>
        </filter>
      </defs>

      <!-- brand lockup -->
      <g class="brand-lockup">
        <circle cx="139" cy="122" r="44" fill="var(--brand-pink)"/>
        <text class="brand-name" x="203" y="118" font-size="40">BRIGHT FERN</text>
        <text class="brand-name" x="205" y="152" font-size="24" letter-spacing="12">REALTY</text>
      </g>

      <!-- name banner -->
      <g class="name-banner">
        <line x1="521" y1="37" x2="584" y2="205" stroke="#d6d6d6" stroke-width="2"/>
        <polygon points="528,63 1050,63 1050,180 572,180" fill="var(--brand-pink)"/>
        <polygon points="527,58 1050,58 1050,63 529,63" fill="var(--brand-blue)"/>
        <polygon points="572,180 1050,180 1050,185 574,185" fill="var(--brand-blue)"/>
        <text class="agent-name" x="805" y="147" text-anchor="middle">MAREN HOLT</text>
      </g>

      <!-- colour steps -->
      <g class="colour-steps">
        <polygon points="746,520 909,520 943,600 780,600" fill="var(--accent-blue)" filter="url(#block-shadow)"/>
        <polygon points="520,405 701,405 773,600 580,600" fill="var(--accent-green)" filter="url(#block-shadow)"/>
        <polygon points="0,349 501,349 586,600 0,600" fill="var(--brand-pink)" filter="url(#block-shadow)"/>
      </g>

      <!-- contact details -->
      <g class="contact-details">
        <g class="contact-icon">
          <rect x="31" y="425" width="30" height="22"/>
          <polyline points="31,425 46,438 61,425"/>
          <line x1="31" y1="447" x2="43" y2="436"/>
          <line x1="61" y1="447" x2="49" y2="436"/>
        </g>
        <text class="contact-line" x="84" y="445">hello@brightfernrealty.com.au</text>

        <g class="contact-icon">
          <circle cx="46" cy="492" r="14"/>
          <ellipse cx="46" cy="492" rx="6" ry="14"/>
          <line x1="32" y1="492" x2="60" y2="492"/>
          <line x1="35" y1="485" x2="57" y2="485"/>
          <line x1="35" y1="499" x2="57" y2="499"/>
        </g>
        <text class="contact-line" x="84" y="501">brightfernrealty.com.au</text>

        <g class="contact-icon">
          <rect x="37" y="529" width="19" height="36" rx="2"/>
          <line x1="37" y1="535" x2="56" y2="535"/>
          <line x1="37" y1="558" x2="56" y2="558"/>
        </g>
        <text class="contact-line" x="84" y="558">0487 316 252 (SMS)</text>
      </g>
    </svg>
  </div>
</body>
</html>
```